Business Consultant - Pluma 3.0 Website Creation

I need to have a website designed on the Newest Pluma 3.0 for Sitecraft. Very Atttractive, SEO friendly. I already purchased the Theme and therefore could do additional changes, as well as add any media or pictures and enter content once the design is implemented.
IF IT NEEDS CODING I WILL UPGRADE!
OPEN TO INCREASE PAYMENT FOR VALUE OF DESIGN
FUTURE WORK PROMISED TO THE WINNER!

This is for a Business Consulting Company.

# of Pages: 5

With a Vibe: Modern, Young, Impactful and Professional
VIBRANT – Bright – White Back.
PROFESSIONAL
Happy Medium between Masculine and Feminine

Main Focus of the main page is getting the user to the "Work with Me" or the "Services" part and showcasing those services. as well as in the Services Pages
(approx. 3-4 Service Packages)

Website's Purpose is to lead the user to 1. Get to know Company 2. Select their issue and it lead them to a service package that will help them.

(Idea) It would be amazing to service a process under each service. or a creative way to showcase a process.

I have added Documents:

A Website Wireframe document (PLEASE FOLLOW): I explain with Examples how I would like the Main Page designed flow wise. The Document is to be used mostly as a map, and as advice for the design wise, I am open to your creative expertise interpretation as well.
( Also Included Font Info)

I have a attached Couple videos of areas that I liked in certain websites that I discuss in the Website Wireframe Document for the Main Big Banner Carousel.
** The TAVO Kelling & Webpage 7z - Attached Videos are for the Main Banner Carousel **

I also Attached a Mood Board for the Design and Color Inspiration.

And my major Inspirations are as follows:

Top Inspirations:
https://www.quorbelt.com/
https://Tessavanmont.com
http://dorimpike.com/
https://www.gildenvault.com/
https://Marcopelt.com
https://Idakessler.com
https://corwintalby.com/
https://www.ambertosley.com/
https://jorikebamstra.nl/
http://odettaraymill.com/
http://www.rowenaplickett.com/
https://www.brightquillstudio.com/

The photos and content will be added to the final design.

Be CREATIVE ! :)

(THE WINNER WILL WORK WITH ME ON FUTURE CLIENTS)*****

Target Market(s)

Business Owners - Age 25-45 - Professional Service Business Industry

Industry/Entity Type

Business Consultant

Coding

Coded - Design and coding required

Number of Pages Required

5+ page

Font styles to use
Sans Serif
Other font styles liked:
• Combination of Bold San Serif & Handwritten Brush

Colors
00a990
9bcb3c
fbed22
ffffff
9d9d9d
333333

Requirements
Must have
• Main Page Build Out
• - As well as 5 Additional Designed Pages (Document Attached with Design Examples)
• - About me
• - Work with Me
• - Book Me
• - Blog
• - Contact Page
Nice to have
• Additional Requests:
• - Responsive ( Beautiful as a Mobile website as well)
• - I want more of a mobile focus as that is where I expect the most traffic. Mobile users like to act quickly and they also like to scroll if their interest is captured so I want the design to reflect that.
• - Any Blurbs or Text boxes (Offer Shadowing affect)
• - Effects

```html
<!DOCTYPE html>
<html lang="en">
<head>
<meta charset="utf-8">
<title>Work With Me – Services</title>
<link href="https://fonts.googleapis.com/css2?family=Permanent+Marker&family=Source+Sans+Pro:wght@400&display=swap" rel="stylesheet">
<style>
  :root {
    --white: #ffffff;
    --ink: #333333;
    --lime: #9bcb3c;
    --lime-text: #a2cf4f;
    --band: #fafafa;
  }
  html, body {
    margin: 0;
    padding: 0;
    width: 1200px;
    height: 226px;
    overflow: hidden;
    background: var(--white);
  }
  .services {
    position: relative;
    width: 1200px;
    height: 226px;
    background: var(--white);
    overflow: hidden;
  }
  .services__title {
    position: absolute;
    left: 0;
    right: 0;
    top: -32px;
    margin: 0;
    text-align: center;
    font-family: "Permanent Marker", cursive;
    font-weight: 400;
    font-size: 36px;
    letter-spacing: 2px;
    color: var(--ink);
    line-height: 1;
  }
  .services__list {
    position: absolute;
    left: 63px;
    top: 64px;
    margin: 0;
    padding: 0;
    list-style: none;
    display: flex;
    gap: 19px;
  }
  .service-button {
    box-sizing: border-box;
    width: 256px;
    height: 86px;
    border: 2px solid var(--lime);
    border-radius: 2px;
    display: flex;
    align-items: center;
    justify-content: center;
    text-align: center;
    padding: 0 24px;
    font-family: "Source Sans Pro", sans-serif;
    font-size: 19px;
    line-height: 35px;
    color: var(--lime-text);
    text-decoration: none;
  }
  .services__band {
    position: absolute;
    left: 0;
    right: 0;
    top: 190px;
    bottom: 0;
    background: var(--band);
  }
</style>
</head>
<body>
  <section class="services">
    <h2 class="services__title">EXPLORE WHAT MY TEAM CAN</h2>
    <ul class="services__list">
      <li><a class="service-button" href="#business-launch">Work with me: Business Launch</a></li>
      <li><a class="service-button" href="#create-funnel">Work with me: Create your Funnel</a></li>
      <li><a class="service-button" href="#consulting">One - on - One Consulting</a></li>
      <li><a class="service-button" href="#add-ons">Work with me: Create your- Add-ons</a></li>
    </ul>
    <div class="services__band"></div>
  </section>
</body>
</html>
```